依頼詳細
FAXにて協力業者の募集をします。それに伴い、募集チラシの作成をお願いいたします。
記載項目
会社名:株式会社カナメハウス
住所:秋田市外旭川柳原町233番4
TEL:018-857-2916

当社の強み
当社カナメハウスは不動産売買を通じ、中古住宅をご購入して頂きましたお客様へ住
まいのリフォーム提案を行っております。
その中で、当社には「中古住宅専門店すみれや」と云う店舗があり年間 250 組以上の来
店があります。また、年間通じて 80 件以上の中古住宅リフォームを手掛けている不動
産会社です。また、外装専門店ヌリカベ秋田店も当社の店舗です。こちらも通年とおし
て外装塗装・外壁張替えの工事を行っております。
サイズ
A4
ページ数
片面
希望イメージ
シンプル 複雑
単色 カラフル
暗い 明るい
日常 高級
遊び心 厳粛
未来的 伝統的
女性的 男性的
希望する色
白黒
納品ファイル
設定なし
補足説明
すみれやイメージキャラクターを使っていただきたいです。
■ 選んだ理由

会社内で多数決しました。
文字の大きさ、分かりやすさが良かったです。

■ 提案者全員のお礼・コメント

この度は、弊社のコンペ依頼へご参加くださり、誠にありがとうございました。
何度かコンペ依頼しており、また次回依頼した際はよろしくお願いいたします。

```html
<!DOCTYPE html>
<html lang="ja">
<head>
<meta charset="utf-8">
<title>協力業者様募集 | 株式会社カナメハウス</title>
<link rel="stylesheet" href="https://fonts.googleapis.com/css2?family=Noto+Sans+JP:wght@400;500;700;900&display=swap">
<style>
  :root {
    --ink: #222222;
    --banner: #3d3d3d;
    --accent: #1f8fd8;
    --accent-deep: #14639f;
    --panel: #dcdcdc;
    --paper: #ffffff;
    --muted: #555555;
    --mascot: #6fae4a;
  }
  * { margin: 0; padding: 0; box-sizing: border-box; }
  html, body { width: 849px; height: 1200px; overflow: hidden; background: var(--paper); }
  body { font-family: "Noto Sans JP", sans-serif; color: var(--ink); }
  .flyer { position: relative; width: 849px; height: 1200px; background: var(--paper); }

  .record-banner {
    position: absolute; left: 0; top: 14px; width: 720px; height: 66px;
    background: var(--banner); border-radius: 0 33px 33px 0;
    color: var(--paper); font-weight: 900; font-size: 40px; letter-spacing: 0.12em;
    display: flex; align-items: center; padding-left: 46px;
  }
  .record-banner .num { font-size: 50px; margin: 0 10px; }

  .trades {
    position: absolute; left: 20px; top: 100px; height: 420px;
    writing-mode: vertical-rl; font-weight: 900; font-size: 40px; line-height: 1.35;
    letter-spacing: 0.04em;
  }
  .trades p { white-space: nowrap; }

  .reform-emblem { position: absolute; left: 430px; top: 70px; width: 300px; height: 270px; }
  .emblem-title { font-weight: 900; font-size: 38px; fill: var(--accent); }

  .recruit-panel {
    position: absolute; left: 283px; top: 334px; width: 552px; height: 232px;
    background: var(--panel); border-radius: 24px;
    display: flex; flex-direction: column; align-items: center; justify-content: center;
    font-weight: 900; line-height: 1.1;
  }
  .recruit-panel .line1 { font-size: 86px; letter-spacing: 0.02em; }
  .recruit-panel .line2 { font-size: 92px; letter-spacing: 0.2em; margin-top: 8px; }

  .company-intro {
    position: absolute; left: 354px; top: 594px; width: 466px;
    font-size: 19px; font-weight: 500; line-height: 1.62; text-align: justify;
  }

  .mascot {
    position: absolute; left: 10px; top: 720px; width: 260px; height: 320px;
    background: radial-gradient(ellipse at 50% 45%, #9fd07e 0%, var(--mascot) 70%, #4f8c33 100%);
    border-radius: 46% 46% 40% 40%;
  }

  .invite-box {
    position: absolute; left: 240px; top: 948px; width: 595px; height: 113px;
    background: var(--accent); border-radius: 18px;
    color: var(--paper); font-weight: 700; font-size: 32px; line-height: 1.45;
    display: flex; flex-direction: column; justify-content: center; padding-left: 44px;
    letter-spacing: 0.08em;
  }
  .invite-box .second { padding-left: 18px; }

  .footer {
    position: absolute; left: 0; top: 1084px; width: 849px; height: 116px;
    border-top: 3px solid var(--ink); display: flex; align-items: center;
  }
  .contact { width: 430px; padding-left: 24px; }
  .contact .label {
    display: inline-block; background: var(--banner); color: var(--paper);
    font-size: 17px; font-weight: 700; padding: 3px 18px; border-radius: 14px;
  }
  .contact .tel { display: flex; align-items: center; gap: 8px; margin-top: 6px; font-size: 44px; font-weight: 900; letter-spacing: 0.02em; }
  .contact .tel svg { width: 38px; height: 38px; fill: var(--ink); }
  .divider { width: 3px; height: 84px; background: var(--ink); }
  .company { padding-left: 26px; }
  .company .name { font-size: 34px; font-weight: 900; letter-spacing: 0.04em; }
  .company .address { font-size: 20px; font-weight: 500; margin-top: 4px; }
</style>
</head>
<body>
<main class="flyer">
  <div class="record-banner">年間実績<span class="num">80</span>件以上！</div>

  <div class="trades">
    <p>大工　設備　電気　内装</p>
    <p>ハウスクリーニング　畳</p>
    <p>板金　左官　外構工事</p>
    <p>外壁塗装　外壁張り</p>
    <p>ガラスサッシ工事</p>
  </div>

  <svg class="reform-emblem" viewBox="0 0 300 270">
    <defs>
      <path id="emblem-arc" d="M30,140 A120,120 0 0 1 270,140"/>
    </defs>
    <text class="emblem-title"><textPath href="#emblem-arc" startOffset="50%" text-anchor="middle">リフォーム工事</textPath></text>
    <circle cx="150" cy="150" r="100" fill="#e8f3fb" stroke="var(--accent)" stroke-width="4"/>
    <circle cx="150" cy="150" r="78" fill="var(--accent)" role="img" aria-label="握手する二つの手のイラスト"/>
  </svg>

  <section class="recruit-panel">
    <h1 class="line1">協力業者様</h1>
    <p class="line2">募集</p>
  </section>

  <p class="company-intro">当社は、年間250組以上の来店のある当社の中古住宅専門店「すみれや」などを通じ中古住宅をご購入のお客様へリフォーム提案を行っております不動産会社です。その他、当社の外装専門店ヌリカベ秋田店でも通年外壁塗装、張替え工事を行っております。</p>

  <div class="mascot" role="img" aria-label="すみれやのイメージキャラクター"></div>

  <div class="invite-box">
    <p>ぜひ一緒に</p>
    <p class="second">お客様の夢を形にしましょう</p>
  </div>

  <footer class="footer">
    <div class="contact">
      <span class="label">お電話お待ちしております</span>
      <p class="tel">
        <svg viewBox="0 0 24 24" aria-hidden="true"><path d="M6.6 10.8a15.1 15.1 0 0 0 6.6 6.6l2.2-2.2a1 1 0 0 1 1-.25 11.4 11.4 0 0 0 3.6.57 1 1 0 0 1 1 1V20a1 1 0 0 1-1 1A17 17 0 0 1 3 4a1 1 0 0 1 1-1h3.5a1 1 0 0 1 1 1c0 1.25.2 2.45.57 3.57a1 1 0 0 1-.25 1z"/></svg>
        018-857-2916
      </p>
    </div>
    <div class="divider"></div>
    <div class="company">
      <p class="name">株式会社カナメハウス</p>
      <p class="address">秋田市外旭川柳原町233番4</p>
    </div>
  </footer>
</main>
</body>
</html>
```